Design einer ITK Unternehmensbroschüre  Grundlayouts mit Deckblatt gesucht
Design einer ITK Unternehmensbroschüre Grundlayouts mit Deckblatt gesucht
Zielgruppe
ITK Systemlösungen mit Schwerpunkt Kommunikationslösungen
Regionale kleine und mittelständische Unternehmen aus allen Branchen
Aufgabenstellung
Vorlage sollte für den Print und Email Versand vorbereitet sein (A4) als Unternehmensbroschüre, die Designlinie sollte bodenständig und innovativ ausgelegt sein.
Dieses Projekt ist als Projektstart zu bewerten und wird in ein eins zu eins Projekt mit erweiterten Budget fortgeführt.
Es soll dazu dienen ein Grundlayout mit Deckblatt zu erstellen um die richtige Linie / Partner zu finden.
Die Kreativität inklusive Aussuchen von passendem Bildmaterial wird vom Designer erwartet und durch Lizenzen im eins zu eins Projekt im Nachgang verrechnet.

```html
<!DOCTYPE html>
<html lang="de">
<head>
<meta charset="utf-8">
<title>Velunix – Unternehmensbroschüre</title>
<link rel="stylesheet" href="https://fonts.googleapis.com/css2?family=Source+Sans+3:wght@300;400;600&display=swap">
<style>
  :root {
    --brand-blue: #15479b;
    --brand-blue-dark: #0b2d66;
    --paper: #ffffff;
    --paper-grey: #f3f3f3;
    --stage: #ececec;
    --ink: #333333;
    --white: #ffffff;
  }
  * { box-sizing: border-box; margin: 0; padding: 0; }
  html, body {
    width: 1200px; height: 900px; overflow: hidden;
    background: var(--stage);
    font-family: "Source Sans 3", sans-serif;
  }
  .page {
    position: absolute; top: 190px; width: 370px; height: 520px;
    box-shadow: 0 4px 14px rgba(0,0,0,.12);
  }

  /* ---------- Cover ---------- */
  .cover { left: 20px; background: linear-gradient(180deg, #d9d9d9 0%, #f2f2f2 100%); overflow: hidden; }
  .cover__photo {
    position: absolute; left: 0; top: 27px; width: 370px; height: 454px;
    background: linear-gradient(120deg, #3d5f8f 0%, #8ea9cc 45%, #c9d7ea 65%, #4f6f9c 100%);
  }
  .cover__url {
    position: absolute; left: 18px; top: 13px; width: 154px; height: 26px;
    background: var(--brand-blue); color: var(--white);
    font-size: 12.5px; font-weight: 400; line-height: 26px; padding-left: 11px;
  }
  .cover__title-box {
    position: absolute; left: 0; top: 270px; width: 280px; height: 158px;
    background: var(--brand-blue); color: var(--white);
    padding: 50px 0 0 29px; font-size: 17px; font-weight: 300; line-height: 21px;
  }
  .cover__brand {
    position: absolute; left: 280px; top: 428px; width: 90px; height: 53px;
    background: var(--white); display: flex; align-items: center; justify-content: center;
    color: var(--brand-blue); font-size: 15px; font-weight: 400; letter-spacing: .5px;
  }
  .cover__tagline {
    position: absolute; left: 35px; top: 486px;
    color: var(--brand-blue); font-size: 14px; font-weight: 400; letter-spacing: .2px;
  }

  /* ---------- Spread left page ---------- */
  .spread-left { left: 430px; background: linear-gradient(90deg, var(--paper-grey) 0%, var(--paper) 60%, #e8e8e8 100%); }
  .section-head {
    position: absolute; left: 61px; top: 72px; display: flex; align-items: baseline; gap: 12px;
  }
  .section-head__title { color: var(--brand-blue); font-size: 18px; font-weight: 400; }
  .section-head__brand { color: var(--brand-blue); font-size: 12px; font-weight: 400; letter-spacing: .4px; }
  .accent-block {
    position: absolute; left: -14px; top: 99px; width: 67px; height: 177px; background: var(--brand-blue);
  }
  .hero-visual {
    position: absolute; left: 61px; top: 99px; width: 309px; height: 177px;
    background: radial-gradient(circle at 50% 45%, #6fb3ea 0%, #1d5d9c 30%, #0a2a55 70%, #061a38 100%);
  }
  .body-copy {
    font-size: 5.1px; line-height: 6.9px; font-weight: 400; color: var(--ink);
    text-align: justify; hyphens: auto;
  }
  .columns { position: absolute; left: 61px; top: 290px; width: 289px; display: flex; gap: 8px; }
  .columns .body-copy { flex: 1; }

  /* ---------- Spread right page ---------- */
  .spread-right { left: 800px; background: var(--brand-blue); color: var(--white); }
  .offer-head { position: absolute; left: 36px; top: 78px; font-size: 18px; font-weight: 300; }
  .tile {
    position: absolute; width: 145px;
  }
  .tile__visual { height: 106px; }
  .tile__title { font-size: 10px; font-weight: 400; line-height: 12px; margin-top: 9px; }
  .tile .body-copy { color: var(--white); margin-top: 3px; }
  .tile .body-copy p + p { margin-top: 6px; }
  .tile--firewall { left: 36px; top: 99px; }
  .tile--firewall .tile__visual { background: linear-gradient(135deg, #0d2f63 0%, #2f6fb6 55%, #b9c9dc 100%); }
  .tile--mdm { left: 197px; top: 99px; }
  .tile--mdm .tile__visual { background: radial-gradient(circle at 60% 40%, #5ea8ef 0%, #1f5fb8 55%, #0d3274 100%); }
  .vpn-visual {
    position: absolute; left: 36px; top: 377px; width: 145px; height: 120px;
    background: radial-gradient(circle at 50% 50%, #d8f0ff 0%, #5db2ea 40%, #2a78c7 100%);
  }
  .tile--vpn { left: 197px; top: 370px; }
  .tile--vpn .tile__title { margin-top: 0; }
</style>
</head>
<body>

<section class="page cover">
  <div class="cover__photo" role="img" aria-label="Foto: zwei Fachkräfte im Serverraum mit digitalen Symbolen"></div>
  <div class="cover__url">www.velunix-itk.de</div>
  <div class="cover__title-box">Informationstechnologie- und<br>Telekommunikationslösungen</div>
  <div class="cover__brand">VELUNIX</div>
  <div class="cover__tagline">TECHNOLOGISCHE STÄRKEN ERÖFFNEN</div>
</section>

<section class="page spread-left">
  <div class="section-head">
    <h1 class="section-head__title">IT - SECURITY</h1>
    <span class="section-head__brand">VELUNIX</span>
  </div>
  <div class="accent-block"></div>
  <div class="hero-visual" role="img" aria-label="Illustration: digitales Vorhängeschloss in leuchtenden Kreisen"></div>
  <div class="columns">
    <p class="body-copy">IT-Security ist in aller Munde und auch bei uns und unseren Kunden immer wieder ein wichtiges Primärthema. Unter IT-Security versteht man alle Planungen, Maßnahmen und Kontrollen, die dem Schutz der IT dienen. Der Schutz der IT hat drei klassische Ziele: Die Vertraulichkeit der Informationen, die Integrität der Informationen und Systeme sowie die Verfügbarkeit der Informationen und Systeme. Um die Verfügbarkeit und Aufrechterhaltung des gesamten Geschäftsbetriebs zu gewährleisten, ist es unabdingbar, ein belastbares IT-System zu haben, welches es auch vor Ausfällen zu schützen gilt.</p>
    <p class="body-copy">Um das Thema IT-Security zu verstehen, muss man sich daran gewöhnen, dass heutzutage nicht nur die klassischen IT Systeme im Netzwerk geschützt werden müssen, sondern auch die Endpoints im und außerhalb Ihres Netzwerks, die die Nutzer verwenden, darunter PCs, Notebooks, Tablets und Smartphones. Der Teil der IT-Security, der sich mit dem Schutz der Endpoints befasst, wird Endpoint Security genannt. Auch die Betriebssysteme und Anwendungen, die auf den Endgeräten laufen, müssen in der IT-Security berücksichtigt werden. Dies geschieht in der Betriebssystemsicherheit und Applikationssicherheit.</p>
    <p class="body-copy">Unsere starken Technologiepartner sowie unsere geschulten Mitarbeiter beraten Sie gerne zu den neusten Security Lösungen und erarbeiten mit Ihnen zusammen die geeignetste Security Strategie, auf Wunsch zu 100% gemanagt.</p>
  </div>
</section>

<section class="page spread-right">
  <h2 class="offer-head">Folgende Lösungen bieten wir Ihnen an</h2>

  <article class="tile tile--firewall">
    <div class="tile__visual" role="img" aria-label="Foto: Hände auf einer Tastatur mit Security-Schriftzug"></div>
    <h3 class="tile__title">FIREWALLS</h3>
    <div class="body-copy">
      <p>Eine gut funktionierende Firewall kann nicht nur die Existenz eines Unternehmens sichern, sondern auch vor Verlust, Verrat oder Manipulation der internen Daten schützen. Der wirtschaftliche Schaden, der dadurch entstehen kann, ist kaum zu beziffern und oft irreparabel. Selbstverständlich sind Sie als Unternehmen auch verantwortlich für alles, was Ihre Mitarbeiter im Internet aufrufen oder abfragen. Ungeeignete oder unproduktive Web-Inhalte sollten daher ebenfalls unterbunden werden.</p>
      <p>Wir bieten Ihnen eine Vielzahl an Firewall-Lösungen an. Mit unserem Security-Konzept decken wir genau die Punkte ab, welche Sie benötigen.</p>
    </div>
  </article>

  <article class="tile tile--mdm">
    <div class="tile__visual" role="img" aria-label="Foto: Hand tippt auf eine digitale MDM-Oberfläche"></div>
    <h3 class="tile__title">MOBILE DEVICE MANAGEMENT</h3>
    <div class="body-copy">
      <p>Immer mehr Tablets, Handys und Mobile Devices werden in das Firmennetzwerk migriert. Gerade hier lauern oft eine Vielzahl an sicherheitskritischen Themen. Mit einem MDM haben Sie die Möglichkeit, alle Mobile Devices zu kontrollieren und entsprechend zu steuern. Zudem besteht hier die Möglichkeit, Nutzungskonzepte zu erstellen, z.B. die Bereitstellung von Unternehmensanwendungen und freigebenden Apps über einen eignen Appstore oder das Verteilen von Daten, Softwareupdates, Patches und Konfigurationseinstellungen. Aber auch die Sicherung von Daten mittels Verschlüsselung und Passwort-Abfragen sowie die Verwaltung von Mailaccounts sprechen für ein MDM-System.</p>
      <p>Gerade bei Verlust von Daten ist es wichtig, das Thema „unternehmensbezogene Daten“ sauber zu bewältigen. Mit einem MDM-System haben Sie die Möglichkeit, Daten aus der Ferne zu löschen oder das Mobile-Device zu orten.</p>
      <p>Gerne beraten wir Sie zu Ihren Möglichkeiten.</p>
    </div>
  </article>

  <div class="vpn-visual" role="img" aria-label="Illustration: leuchtendes Schutzschild mit VPN über einem Notebook"></div>
  <article class="tile tile--vpn">
    <h3 class="tile__title">VPN<br>VIRTUELL PRIVATE NETWORK</h3>
    <div class="body-copy">
      <p>Mittels VPN erreichen Sie ihre Daten von der ganzen Welt aus. Wie das geht, ist einfach erklärt. Über das Internet wird ein „Tunnel“ zu Ihrem Netzwerk aufgebaut. Dieser Tunnel ist eine verschlüsselte Verbindung zwischen Ihrem Notebook und Ihrem Server. Zum Entschlüsseln der Daten muss ein gemeinsamer Schlüssel vorhanden sein, den nur die beiden Geräte besitzen. Meistens ist eines von beiden Geräten eine Hardware-Firewall und das andere ein mobiles Endgerät, was die Mobilität einzelner Mitarbeiter erhöht. Es können aber auch zwei oder mehrere Hardware-Firewalls untereinander Tunnel aufbauen, um eine Standortvernetzung zu erreichen. Wir bieten Ihnen mit unseren starken Technologiepartnern eine Vielzahl an Lösungen für jede IT Umgebung.</p>
    </div>
  </article>
</section>

</body>
</html>
```